Tess Marlowe Communication business card

I am starting a small, country-based business that offers writing, communication and marketing services to a wide range of clients, inner city big business, to mining, through to agriculture.

The appeal of my business is that it's mobile and flexible. It's just me, with lots of hands-on experience on construction and infrastructure projects.

I can provide the following services:

• Communication planning and management
• Issues and media management
• Marketing and communication materials
• Project management and strategy
• Government liaison
• Incident management communication
• Stakeholder management

It would be great to be able to use the elements of the business card design on other stationery.

Industry/Entity Type

Communication

Requirements
Must have
• The following information:

Tess Marlowe
M: 0427 391 864
E: tess@tmcommsmail.com

PO Box 152
Durrandale Q 4472
Nice to have
• a rural element (windmill, workboots, wheat stalk)

```html
<!DOCTYPE html>
<html lang="en">
<head>
<meta charset="utf-8">
<title>Tess Marlowe Communication – Business Card</title>
<link href="https://fonts.googleapis.com/css2?family=Mulish:wght@400;700;800&display=swap" rel="stylesheet">
<style>
  :root {
    --green: #8cc63f;
    --green-deep: #5f9e2a;
    --green-frame: #3d8a2a;
    --ink-dark: #161616;
    --ink-mid: #3c3c3c;
    --paper: #ffffff;
    --backdrop: #e9e7e2;
    --corner-block: #1e2a18;
  }
  * { box-sizing: border-box; margin: 0; padding: 0; }
  html, body {
    width: 1200px; height: 900px; overflow: hidden;
    background: var(--backdrop);
    font-family: "Mulish", sans-serif;
  }
  .canvas { position: relative; width: 1200px; height: 900px; }

  .card {
    position: absolute; left: 290px;
    width: 620px; height: 354px;
    overflow: hidden;
    box-shadow: 0 6px 18px rgba(0,0,0,.22);
  }
  .card--front { top: 78px;
    background: radial-gradient(ellipse at 55% 45%, var(--ink-mid) 0%, var(--ink-dark) 75%);
  }
  .card--back { top: 470px; background: var(--paper); }

  .band { position: absolute; left: 0; width: 100%; background: linear-gradient(180deg, var(--green) 0%, var(--green-deep) 100%); }
  .card--front .band--top { top: 0; height: 28px; }
  .card--front .band--bottom { bottom: 0; height: 28px; }
  .card--back .band--bottom { bottom: 0; height: 50px; }
  .corner-block { position: absolute; right: 0; bottom: 50px; width: 34px; height: 22px; background: var(--corner-block); }

  .brand {
    position: absolute; left: 40px;
    color: var(--green); font-weight: 800;
    text-transform: uppercase; letter-spacing: .5px;
  }
  .card--front .brand { top: 42px; font-size: 25px; }
  .card--back .brand { top: 40px; font-size: 25px; }

  .photo {
    position: absolute; width: 125px; height: 102px;
    border: 4px solid var(--green-frame);
    box-shadow: 0 0 0 1px var(--green);
  }
  .photo--wheat { left: 40px; top: 150px; background: linear-gradient(160deg, #c99a4e, #7a5524); }
  .photo--windmill { left: 180px; top: 92px; background: linear-gradient(180deg, #3f7fd0 0%, #8db6e6 60%, #4d7a33 100%); }
  .photo--boots { left: 200px; top: 206px; background: linear-gradient(170deg, #5d77a0 0%, #9c8463 55%, #6e5a40 100%); }

  .contact { position: absolute; left: 392px; top: 104px; color: var(--green); }
  .contact__name { font-size: 20px; font-weight: 800; margin-bottom: 10px; }
  .contact__line { font-size: 15px; line-height: 1.45; opacity: .9; }
  .email { position: absolute; right: 40px; bottom: 40px; color: var(--green); font-size: 15px; }

  .services { position: absolute; left: 40px; top: 80px; color: var(--green); }
  .services__intro { font-size: 15px; margin-bottom: 8px; }
  .services__list { list-style: none; font-size: 14.5px; line-height: 1.3; }
  .services__list li::before { content: "• "; }
</style>
</head>
<body>
<main class="canvas">
  <section class="card card--front" aria-label="Business card front">
    <div class="band band--top"></div>
    <h1 class="brand">Tess Marlowe Communication</h1>
    <div class="photo photo--wheat" role="img" aria-label="Photo of ripe wheat stalks"></div>
    <div class="photo photo--windmill" role="img" aria-label="Photo of a windmill against blue sky"></div>
    <div class="photo photo--boots" role="img" aria-label="Photo of work boots and jeans on dry ground"></div>
    <div class="contact">
      <p class="contact__name">Tess Marlowe</p>
      <p class="contact__line">Mobile : 0427 391 864</p>
      <p class="contact__line">Durrandale Q 4472</p>
      <p class="contact__line">PO Box 152</p>
    </div>
    <p class="email">tess@tmcommsmail.com</p>
    <div class="band band--bottom"></div>
  </section>

  <section class="card card--back" aria-label="Business card back">
    <h2 class="brand">Tess Marlowe Communication</h2>
    <div class="services">
      <p class="services__intro">We provide the following services:</p>
      <ul class="services__list">
        <li>Communication planning and management</li>
        <li>Issues and media management</li>
        <li>Marketing and communication materials</li>
        <li>Project management and strategy</li>
        <li>Government liaison</li>
        <li>Incident management communication</li>
        <li>Stakeholder management</li>
      </ul>
    </div>
    <div class="corner-block"></div>
    <div class="band band--bottom"></div>
  </section>
</main>
</body>
</html>
```